pressure washing advertisment

I would like front and back designed post cards. we offer pressure washing services for residential customers. I want to highlight before and after pictures as examples of our more popular services. I would also like to have our email www.brightlanewashco.com and the facebook and Instagram logo somewhere. you can also include all major credit card logos as acceptable payments. I have attached our logo along with before and after pictures. also feel free to go to my website for any additional information that should be added to the post card. lastly I want a small promotion of $25 off any service somewhere.<br/><br/>Thank you!!

Target Market(s)

homeowners

Industry/Entity Type

Cleaning Service

Font styles to use
Serif
Sans Serif

Colors

Designer to choose colors to be used in the design.

Requirements
Must have
• before and after pictures with website and logo
Nice to have
• clean look that flows

```html
<!DOCTYPE html>
<html lang="en">
<head>
<meta charset="utf-8">
<title>Brightlane Wash Co — Postcards</title>
<link rel="stylesheet" href="https://fonts.googleapis.com/css2?family=Oswald:wght@400;500&family=Roboto:wght@500&display=swap">
<style>
  :root{
    --navy:#1d3d78;
    --navy-deep:#12295a;
    --red:#d0202a;
    --red-deep:#9c1018;
    --red-edge:#b3312f;
    --paper:#ececec;
    --paper-shade:#d6d6d6;
    --ink:#1f3a73;
    --tick:#2f5ea8;
    --text-dark:#222;
    --gold:#f3c534;
    --white:#fff;
  }
  *{margin:0;padding:0;box-sizing:border-box}
  html,body{width:1200px;height:3600px;overflow:hidden}
  body{background:var(--navy);font-family:'Oswald',sans-serif;position:relative}

  .postcard{position:absolute;left:30px;width:1140px;height:758px;background:var(--paper);overflow:hidden;box-shadow:0 6px 18px rgba(0,0,0,.35)}
  .postcard--front{top:980px}
  .postcard--back{top:1862px}
  .postcard__art{position:absolute;inset:0;width:1140px;height:758px}

  .brand{position:absolute;display:flex;align-items:center;gap:10px;color:var(--ink);font-weight:500;font-size:26px;letter-spacing:1px;line-height:1}
  .brand__dot{width:18px;height:18px;border-radius:50%;background:var(--red)}

  .headline{position:absolute;color:var(--red);font-weight:500;font-size:64px;letter-spacing:9px;line-height:1;white-space:nowrap}
  .subhead{position:absolute;color:var(--ink);font-weight:400;font-size:36px;letter-spacing:7px;line-height:1.15;white-space:nowrap}
  .subhead--red{color:var(--red);font-size:30px;letter-spacing:3px}

  .services{position:absolute;list-style:none;display:grid;grid-template-columns:auto auto;column-gap:28px;row-gap:12px}
  .services li{display:flex;align-items:center;gap:12px;color:var(--text-dark);font-size:17px;letter-spacing:1.5px;line-height:24px;white-space:nowrap}
  .services--back li{font-size:16px;letter-spacing:1.2px}
  .services svg{width:24px;height:24px;flex:none}

  .offer{position:absolute;width:256px;height:256px;display:flex;flex-direction:column;align-items:center;justify-content:center;color:var(--white);font-family:'Roboto',sans-serif;font-weight:500;font-size:72px;line-height:1}

  .contact{position:absolute;text-align:center;color:var(--white);white-space:nowrap}
  .contact__label{font-size:22px;line-height:28px;letter-spacing:2px}
  .contact__phone{font-size:38px;line-height:46px;font-weight:500;letter-spacing:3px}
  .contact__address{font-size:23px;line-height:32px;letter-spacing:2px}

  .web{position:absolute;display:flex;justify-content:center;gap:40px;font-size:18px;line-height:22px;letter-spacing:1.5px;color:var(--text-dark);white-space:nowrap}
  .web--gold{color:var(--gold);font-size:17px}
</style>
</head>
<body>

<section class="postcard postcard--front">
  <svg class="postcard__art" viewBox="0 0 1140 758">
    <defs>
      <linearGradient id="photoFront" x1="0" y1="0" x2="1" y2="1">
        <stop offset="0" stop-color="#c9c2a4"/><stop offset=".5" stop-color="#8b8f7c"/><stop offset="1" stop-color="#2a3f6e"/>
      </linearGradient>
      <linearGradient id="bandFront" x1="0" y1="0" x2="1" y2="0">
        <stop offset="0" stop-color="#12295a"/><stop offset="1" stop-color="#1d3d78"/>
      </linearGradient>
      <radialGradient id="badgeFront" cx=".4" cy=".35" r=".7">
        <stop offset="0" stop-color="#d0202a"/><stop offset="1" stop-color="#9c1018"/>
      </radialGradient>
    </defs>
    <path d="M0 720 C180 590 430 540 1140 525 L1140 720 Z" fill="url(#bandFront)"/>
    <path d="M0 758 C250 730 500 722 760 722 L760 727 C500 728 250 738 0 758 Z" fill="#d6d6d6"/>
    <path d="M612 0 C720 150 770 320 740 470 L720 758 L1140 758 L1140 0 Z" fill="#b3312f"/>
    <path role="img" aria-label="Photo of a house being pressure washed with a smiling man in a suit, arms crossed" d="M632 0 C735 150 785 320 755 470 L735 758 L1140 758 L1140 0 Z" fill="url(#photoFront)"/>
    <circle cx="145" cy="580" r="128" fill="#fff"/>
    <circle cx="145" cy="580" r="118" fill="url(#badgeFront)"/>
  </svg>

  <div class="brand" style="left:55px;top:36px"><span class="brand__dot"></span>BRIGHTLANE WASH CO</div>
  <h1 class="headline" style="left:55px;top:172px">PROFESSIONAL</h1>
  <p class="subhead" style="left:58px;top:255px">RESIDENTIAL PRESSURE<br>WASHING SURVICE</p>
  <ul class="services" style="left:50px;top:380px">
    <li><svg viewBox="0 0 24 24"><circle cx="12" cy="12" r="10" fill="none" stroke="#2f5ea8" stroke-width="2.5"/><path d="M7 12l4 4 7-8" fill="none" stroke="#2f5ea8" stroke-width="2.5"/></svg>SOFT WASH HOUSE WASHING</li>
    <li><svg viewBox="0 0 24 24"><circle cx="12" cy="12" r="10" fill="none" stroke="#2f5ea8" stroke-width="2.5"/><path d="M7 12l4 4 7-8" fill="none" stroke="#2f5ea8" stroke-width="2.5"/></svg>DRIVEWAY &amp; CONCRETE CLEANING</li>
    <li><svg viewBox="0 0 24 24"><circle cx="12" cy="12" r="10" fill="none" stroke="#2f5ea8" stroke-width="2.5"/><path d="M7 12l4 4 7-8" fill="none" stroke="#2f5ea8" stroke-width="2.5"/></svg>GUTTER CLEANING &amp; BRIGHTENING</li>
    <li><svg viewBox="0 0 24 24"><circle cx="12" cy="12" r="10" fill="none" stroke="#2f5ea8" stroke-width="2.5"/><path d="M7 12l4 4 7-8" fill="none" stroke="#2f5ea8" stroke-width="2.5"/></svg>DECK &amp; FENCE CLEANING</li>
  </ul>
  <div class="offer" style="left:17px;top:452px"><span>$25</span><span>OFF</span></div>
  <div class="contact" style="left:172px;top:600px;width:600px">
    <p class="contact__label">CALL US TODAY</p>
    <p class="contact__phone">555-214-0387</p>
    <p class="contact__address">41 HARBOR PINE RD CORAL BAY, FL 32190</p>
  </div>
  <div class="web" style="left:80px;top:730px;width:640px"><span>WWW.BRIGHTLANEWASHCO.COM</span><span>HELLO@BRIGHTLANEWASHCO.COM</span></div>
</section>

<section class="postcard postcard--back">
  <svg class="postcard__art" viewBox="0 0 1140 758">
    <defs>
      <linearGradient id="photoBack" x1="0" y1="0" x2="1" y2="1">
        <stop offset="0" stop-color="#9fb2c4"/><stop offset=".5" stop-color="#7d95b2"/><stop offset="1" stop-color="#2c2f36"/>
      </linearGradient>
      <linearGradient id="bandBack" x1="0" y1="0" x2="1" y2="0">
        <stop offset="0" stop-color="#12295a"/><stop offset="1" stop-color="#1d3d78"/>
      </linearGradient>
      <radialGradient id="badgeBack" cx=".4" cy=".35" r=".7">
        <stop offset="0" stop-color="#d0202a"/><stop offset="1" stop-color="#9c1018"/>
      </radialGradient>
    </defs>
    <path d="M0 0 L545 0 C595 130 585 290 490 412 L0 540 Z" fill="#b3312f"/>
    <path role="img" aria-label="Photo of two crew members in work shirts standing by a pressure washing rig" d="M0 0 L522 0 C570 130 560 280 470 400 L0 520 Z" fill="url(#photoBack)"/>
    <path d="M0 538 C300 470 650 455 1110 475 L1110 485 C700 470 330 495 0 558 Z" fill="#d6d6d6"/>
    <path d="M0 560 C320 485 700 470 1060 505 L1060 712 L0 712 Z" fill="url(#bandBack)"/>
    <circle cx="138" cy="490" r="128" fill="#fff"/>
    <circle cx="138" cy="490" r="118" fill="url(#badgeBack)"/>
    <g class="payment-cards" stroke="#fff" stroke-width="1">
      <rect x="20" y="718" width="50" height="32" rx="3" fill="#283e70"/>
      <rect x="76" y="718" width="50" height="32" rx="3" fill="#2f8a7c"/>
      <rect x="132" y="718" width="50" height="32" rx="3" fill="#222"/>
      <rect x="188" y="718" width="50" height="32" rx="3" fill="#365a96"/>
      <rect x="244" y="718" width="50" height="32" rx="3" fill="#1e2c4f"/>
      <rect x="300" y="718" width="50" height="32" rx="3" fill="#8b2020"/>
      <rect x="356" y="718" width="50" height="32" rx="3" fill="#3a60a8"/>
      <rect x="412" y="718" width="50" height="32" rx="3" fill="#e1b53b"/>
      <rect x="468" y="718" width="50" height="32" rx="3" fill="#8fb3dc"/>
      <rect x="524" y="718" width="50" height="32" rx="3" fill="#d5d5d5"/>
      <rect x="580" y="718" width="50" height="32" rx="3" fill="#283e70"/>
      <rect x="636" y="718" width="50" height="32" rx="3" fill="#2f8a7c"/>
      <rect x="692" y="718" width="50" height="32" rx="3" fill="#222"/>
      <rect x="748" y="718" width="50" height="32" rx="3" fill="#365a96"/>
      <rect x="804" y="718" width="50" height="32" rx="3" fill="#1e2c4f"/>
      <rect x="860" y="718" width="50" height="32" rx="3" fill="#8b2020"/>
      <rect x="916" y="718" width="50" height="32" rx="3" fill="#3a60a8"/>
      <rect x="972" y="718" width="50" height="32" rx="3" fill="#e1b53b"/>
    </g>
  </svg>

  <div class="brand" style="left:610px;top:40px"><span class="brand__dot"></span>BRIGHTLANE WASH CO</div>
  <h1 class="headline" style="right:31px;top:158px">PROFESSIONAL</h1>
  <p class="subhead" style="right:24px;top:232px">RESIDENTIAL PRESSURE</p>
  <p class="subhead" style="left:752px;top:274px">WASHING</p>
  <p class="subhead subhead--red" style="right:42px;top:344px">SURVICE</p>
  <ul class="services services--back" style="left:520px;top:392px">
    <li><svg viewBox="0 0 24 24"><circle cx="12" cy="12" r="10" fill="none" stroke="#2f5ea8" stroke-width="2.5"/><path d="M7 12l4 4 7-8" fill="none" stroke="#2f5ea8" stroke-width="2.5"/></svg>SOFT WASH HOUSE WASHING</li>
    <li><svg viewBox="0 0 24 24"><circle cx="12" cy="12" r="10" fill="none" stroke="#2f5ea8" stroke-width="2.5"/><path d="M7 12l4 4 7-8" fill="none" stroke="#2f5ea8" stroke-width="2.5"/></svg>DRIVEWAY &amp; CONCRETE CLEANING</li>
    <li><svg viewBox="0 0 24 24"><circle cx="12" cy="12" r="10" fill="none" stroke="#2f5ea8" stroke-width="2.5"/><path d="M7 12l4 4 7-8" fill="none" stroke="#2f5ea8" stroke-width="2.5"/></svg>GUTTER CLEANING &amp; BRIGHTENING</li>
    <li><svg viewBox="0 0 24 24"><circle cx="12" cy="12" r="10" fill="none" stroke="#2f5ea8" stroke-width="2.5"/><path d="M7 12l4 4 7-8" fill="none" stroke="#2f5ea8" stroke-width="2.5"/></svg>DECK &amp; FENCE CLEANING</li>
  </ul>
  <div class="offer" style="left:10px;top:362px"><span>$25</span><span>OFF</span></div>
  <div class="contact" style="left:120px;top:572px;width:600px">
    <p class="contact__label">CALL US TODAY</p>
    <p class="contact__phone">555-214-0387</p>
    <p class="contact__address">41 HARBOR PINE RD CORAL BAY, FL 32190</p>
  </div>
  <div class="web web--gold" style="left:120px;top:684px;width:600px"><span>WWW.BRIGHTLANEWASHCO.COM</span><span>HELLO@BRIGHTLANEWASHCO.COM</span></div>
</section>

</body>
</html>
```